Business Cards - Brightwell Harbor

need to design unique business card for my mortgage business. I need to design credit card style business card for my business or any unique idea that you might have

Target Market(s)

Home Loan customers

Industry/Entity Type

Mortgage Brokerage

Contact Information for Business Card

please design credit card style or very unique style business card

Colors

Designer to choose colors to be used in the design.

Requirements
Must have
• Name
• position
• Phone number
• fax number
• email address
• website address
• social media address
• All above fields will be provided once design in finalised

```html
<!DOCTYPE html>
<html lang="en">
<head>
<meta charset="utf-8">
<title>Brightwell Harbor – Business Cards</title>
<link href="https://fonts.googleapis.com/css2?family=Open+Sans:wght@400;600;700&family=Lora:ital@1&display=swap" rel="stylesheet">
<style>
  :root {
    --stage: #000000;
    --card: #3a3a3d;
    --card-edge: #444448;
    --ink: #ffffff;
    --ink-soft: #e6e6e6;
    --rule: #6a6a6e;
    --icon-cut: #3a3a3d;
  }
  * { margin: 0; padding: 0; box-sizing: border-box; }
  html, body { width: 1200px; height: 900px; overflow: hidden; background: var(--stage); }
  .stage { position: relative; width: 1200px; height: 900px; font-family: "Open Sans", Arial, sans-serif; color: var(--ink); }
  .card {
    position: absolute; top: 271px; width: 457px; height: 281px;
    background: radial-gradient(ellipse at 50% 40%, var(--card-edge), var(--card) 70%);
    border-radius: 14px;
  }
  .card--front { left: 137px; }
  .card--back { left: 626px; }

  .brand { position: absolute; text-align: center; font-weight: 600; color: var(--ink); line-height: 1; }
  .brand__name-top { display: block; font-size: 19px; letter-spacing: 2px; }
  .brand__name-main { display: block; font-size: 31px; letter-spacing: 1px; margin-top: 5px; }
  .brand__tagline { display: block; font-family: "Lora", Georgia, serif; font-style: italic; font-weight: 400; font-size: 12px; margin-top: 6px; }
  .card--front .brand { left: 44px; top: 118px; width: 190px; }
  .card--back .brand { left: 128px; top: 114px; width: 200px; }

  .divider { position: absolute; left: 251px; top: 70px; width: 1px; height: 147px; background: var(--rule); }

  .person { position: absolute; left: 267px; top: 79px; }
  .person__name { font-size: 16px; font-weight: 600; line-height: 20px; }
  .person__role { font-size: 12.5px; color: var(--ink-soft); line-height: 16px; }

  .contacts { position: absolute; left: 268px; top: 141px; list-style: none; }
  .contacts li { display: flex; align-items: center; height: 19px; font-size: 12.5px; color: var(--ink-soft); white-space: nowrap; }
  .contacts svg { width: 10px; height: 10px; margin-right: 6px; fill: var(--ink); flex: none; }

  .social { position: absolute; left: 179px; top: 214px; display: flex; gap: 9px; }
  .social__dot { width: 27px; height: 27px; border-radius: 50%; background: var(--ink); }
</style>
</head>
<body>
<div class="stage">
  <section class="card card--front">
    <div class="brand">
      <span class="brand__name-top">BRIGHTWELL</span>
      <span class="brand__name-main">HARBOR</span>
      <span class="brand__tagline">Sound plans, Safe homes</span>
    </div>
    <div class="divider"></div>
    <div class="person">
      <p class="person__name">Daniel Marsh</p>
      <p class="person__role">Managing Director</p>
    </div>
    <ul class="contacts">
      <li><svg viewBox="0 0 10 10"><path d="M2 0.5 L3.6 2.6 L2.7 3.6 Q3.6 5.6 6.4 7.3 L7.4 6.4 L9.5 8 L8.4 9.5 Q4.5 9.2 0.5 1.6 Z"/></svg>(052)-318-4476</li>
      <li><svg viewBox="0 0 10 10"><rect x="2.5" y="0.5" width="5" height="3"/><rect x="0.5" y="3.5" width="9" height="4.5" rx="0.8"/><rect x="2.5" y="7" width="5" height="2.5"/></svg>318-552-0194</li>
      <li><svg viewBox="0 0 10 10"><path d="M0.5 2 H9.5 V8.5 H0.5 Z M1.2 2.6 L5 5.6 L8.8 2.6" stroke="var(--icon-cut)" stroke-width="0.8"/></svg>hello@brightwell.co</li>
      <li><svg viewBox="0 0 10 10"><circle cx="5" cy="5" r="4.6"/><path d="M5 0.5 V9.5 M0.5 5 H9.5" stroke="var(--icon-cut)" stroke-width="0.7"/></svg>www.brightwell.co</li>
    </ul>
  </section>

  <section class="card card--back">
    <div class="brand">
      <span class="brand__name-top">BRIGHTWELL</span>
      <span class="brand__name-main">HARBOR</span>
      <span class="brand__tagline">Sound plans, Safe homes</span>
    </div>
    <div class="social" aria-label="Social media links">
      <span class="social__dot"></span>
      <span class="social__dot"></span>
      <span class="social__dot"></span>
    </div>
  </section>
</div>
</body>
</html>
```